RTB Weissbier: Art NOUVEAU Illustration & Beer Label

We want your help for a really exquisite project.
We are to launch a traditional weissbier with very noble Mitteleuropa pedigree.

Name: RTB
...from Reinhold Tobias Baumgart, the last Austro-Hungarian emperor.
https://en.quellarchiv.example/wiki/Reinhold_Tobias_Baumgart

We want to play on the letters RTB (with their dual meaning) and the iconic figure of the emperor. Illustration skills are absolutely critical. We want this to look like 1900-1914 avant-garde. See attached references for the emperor figure and some feel references for the epoque.

This beer is a traditional Weissbier born in Lindgrube, in a craft Bavarian brewery that dates from 1853.

Target Market(s)

Europe

Colors

Designer to choose colors to be used in the design.

Requirements
Must have
• Illustration of the Emperor in great art deco style
• Should look more like a painting / poster than a computer made vectorial
• Practicalities as per attached file
Nice to have
• The emperor appreciating a glass of his Weissbier
• RTB the beer name written with great Art Deco fonts, looking like it was handcrafted
• Faded blue tones & yolk yellow.

```html
<!DOCTYPE html>
<html lang="en">
<head>
<meta charset="utf-8">
<title>RTB Hefe Weissbier – Label Designs</title>
<link rel="stylesheet" href="https://fonts.googleapis.com/css2?family=Federo&family=Fascinate&family=Arimo:wght@400;700&family=Cinzel:wght@700&display=swap">
<style>
  :root {
    --canvas: #ffffff;
    --paper: #ffffff;
    --ink: #1d1d1f;
    --blue-ink: #3a5468;
    --blue-soft: #cfe3e8;
    --blue-pale: #e6f1f3;
    --blue-frame: #9fb4bf;
    --yolk: #f4b01b;
    --yolk-soft: #fbd46a;
    --grey-frame: #9a9a9a;
    --portrait-light: #d9d9d9;
    --portrait-dark: #6d6d6d;
  }
  * { box-sizing: border-box; margin: 0; padding: 0; }
  html, body { width: 1200px; height: 900px; overflow: hidden; background: var(--canvas); }
  .canvas { position: relative; width: 1200px; height: 900px; }

  .variant { position: absolute; top: 70px; width: 360px; display: flex; flex-direction: column; align-items: center; gap: 40px; }
  .variant--blue { left: 120px; }
  .variant--yolk { left: 720px; }

  /* Neck label */
  .neck-label {
    width: 190px; height: 110px; background: var(--paper);
    display: flex; flex-direction: column; align-items: center; justify-content: center; gap: 4px;
    border: 1px solid #e4e4e4;
  }
  .neck-label .medallion { width: 44px; height: 52px; border-radius: 50%; }
  .neck-label .neck-year { font: 700 8px "Cinzel", serif; color: var(--ink); letter-spacing: 1px; }
  .neck-label .neck-name { font-size: 28px; line-height: 1; }

  /* Main label */
  .main-label {
    position: relative; width: 360px; height: 500px; background: var(--paper);
    padding: 14px;
  }
  .variant--blue .main-label { border: 5px solid var(--blue-pale); }
  .variant--yolk .main-label { border: 9px solid var(--yolk); }

  .frame { position: absolute; inset: 12px; width: calc(100% - 24px); height: calc(100% - 24px); }

  .label-body {
    position: relative; height: 100%;
    display: flex; flex-direction: column; align-items: center;
    padding: 12px 26px 16px;
  }
  .arch { width: 180px; height: 34px; }
  .arch text { font: 700 11px "Cinzel", serif; letter-spacing: 1.5px; }

  .portrait-wreath {
    width: 170px; height: 170px; border-radius: 50% 50% 46% 46%;
    margin-top: -4px;
  }
  .variant--blue .portrait-wreath, .variant--blue .medallion {
    background: radial-gradient(ellipse 38% 44% at 50% 46%, var(--portrait-light) 0%, var(--portrait-dark) 70%, var(--portrait-dark) 82%, var(--blue-soft) 84%, #ffffff 100%);
  }
  .variant--yolk .portrait-wreath, .variant--yolk .medallion {
    background: radial-gradient(ellipse 38% 44% at 50% 46%, var(--portrait-light) 0%, var(--portrait-dark) 70%, var(--portrait-dark) 82%, var(--yolk-soft) 84%, #ffffff 100%);
  }

  .year { font: 700 13px "Cinzel", serif; letter-spacing: 2px; margin-top: 2px; }
  .beer-name { line-height: 1; margin-top: 4px; }
  .variant--blue .beer-name, .variant--blue .neck-name { font-family: "Federo", sans-serif; color: var(--blue-ink); }
  .variant--yolk .beer-name, .variant--yolk .neck-name { font-family: "Fascinate", cursive; color: var(--ink); }
  .variant--blue .beer-name { font-size: 92px; letter-spacing: 2px; }
  .variant--yolk .beer-name { font-size: 82px; }
  .variant--blue .year { color: var(--blue-ink); }
  .variant--yolk .year { color: var(--ink); }

  .style-name { font: 700 15px "Cinzel", serif; letter-spacing: 2px; margin-top: 6px; }
  .variant--blue .style-name { color: var(--blue-frame); }
  .variant--yolk .style-name { color: var(--yolk); }

  .story { font: 400 10.5px/1.35 "Arimo", sans-serif; color: var(--ink); text-align: center; margin-top: 10px; }

  .facts {
    width: 100%; display: flex; justify-content: space-between;
    font: 400 10px "Arimo", sans-serif; color: var(--ink); margin-top: auto;
  }
</style>
</head>
<body>
<main class="canvas">

  <!-- Faded blue edition -->
  <section class="variant variant--blue" aria-label="RTB Hefe Weissbier, faded blue label">
    <div class="neck-label">
      <div class="medallion" role="img" aria-label="Small oval engraved-style portrait medallion in a blue laurel wreath"></div>
      <span class="neck-year">1853</span>
      <span class="neck-name">RTB</span>
    </div>
    <article class="main-label">
      <svg class="frame" viewBox="0 0 312 452" preserveAspectRatio="none" aria-hidden="true">
        <g fill="none" stroke="var(--blue-frame)" stroke-width="1.5">
          <path d="M14 2 H298 V14 H310 V438 H298 V450 H14 V438 H2 V14 H14 Z"/>
          <path d="M20 8 H292 V20 H304 V432 H292 V444 H20 V432 H8 V20 H20 Z" stroke-width="0.8"/>
        </g>
      </svg>
      <div class="label-body">
        <svg class="arch" viewBox="0 0 180 34" aria-label="Craft Bavarian">
          <defs><path id="arch-blue" d="M20 32 Q90 -6 160 32"/></defs>
          <text fill="var(--blue-frame)" text-anchor="middle"><textPath href="#arch-blue" startOffset="50%">CRAFT BAVARIAN</textPath></text>
        </svg>
        <div class="portrait-wreath" role="img" aria-label="Oval vintage portrait illustration framed by a faded blue laurel wreath"></div>
        <span class="year">1853</span>
        <h2 class="beer-name">RTB</h2>
        <p class="style-name">HEFE WEISSBIER</p>
        <p class="story">Weissbier born in Lindgrube, in a craft Bavarian<br>brewery that dates from 1853.</p>
        <div class="facts"><span>alk. 4,9% vol</span><span>e 0,5 l</span></div>
      </div>
    </article>
  </section>

  <!-- Yolk yellow edition -->
  <section class="variant variant--yolk" aria-label="RTB Hefe Weissbier, yolk yellow label">
    <div class="neck-label">
      <div class="medallion" role="img" aria-label="Small oval engraved-style portrait medallion in a yellow wheat wreath"></div>
      <span class="neck-year">1853</span>
      <span class="neck-name">RTB</span>
    </div>
    <article class="main-label">
      <svg class="frame" viewBox="0 0 312 452" preserveAspectRatio="none" aria-hidden="true">
        <g fill="none" stroke="var(--grey-frame)" stroke-width="1.2">
          <path d="M14 2 H298 V14 H310 V438 H298 V450 H14 V438 H2 V14 H14 Z"/>
          <path d="M20 8 H292 V20 H304 V432 H292 V444 H20 V432 H8 V20 H20 Z" stroke-width="0.7"/>
        </g>
      </svg>
      <div class="label-body">
        <svg class="arch" viewBox="0 0 180 34" aria-label="Craft Bavarian">
          <defs><path id="arch-yolk" d="M20 32 Q90 -6 160 32"/></defs>
          <text fill="var(--ink)" text-anchor="middle"><textPath href="#arch-yolk" startOffset="50%">CRAFT BAVARIAN</textPath></text>
        </svg>
        <div class="portrait-wreath" role="img" aria-label="Oval vintage portrait illustration framed by a yolk yellow wheat wreath"></div>
        <span class="year">1853</span>
        <h2 class="beer-name">RTB</h2>
        <p class="style-name">HEFE WEISSBIER</p>
        <p class="story">Weissbier born in Lindgrube, in a craft Bavarian<br>brewery that dates from 1853.</p>
        <div class="facts"><span>alk. 4,9% vol</span><span>e 0,5 l</span></div>
      </div>
    </article>
  </section>

</main>
</body>
</html>
```